Plum Stride Buisiness card

needing a Business card for our company - Plum Stride.
Plum stride is co owned by Nell and Dermot Wardrop (Husband and Wife)
Services Plum Stride provides include:
Dietetic/nutrition Consultations, weight loss coaching programs, personal and group training, post injury rehab, health and nutrition presentations and Health Retreats.
Nell:
Accredited Practicing Dietitian & Personal trainer
Dermot:
Personal trainer, rehab trainer & Strength and conditioning coach
At this stage the business cards will be made just for Nell.
She has a training studio in Armadale and Dietetics private practice in Richmond.
Mobile services are also available (i.e. meet at house or local cafe)

We need the card to look smart, modern and combine both nutrition and training.
We already have a logo which I will attach.
I was initial thinking i black background but am open to suggestions.

Target Market(s)

Health concious, People with money,

Industry/Entity Type

Nutrition

Contact Information for Business Card

Plum Stride
Nell Wardrop
M: 0431907265
E: plumstride@postwren.com
W: www.plumstride.com.au
Address:
Dietetics: Level 1, 88 Tolley Street
Richmond VIC 3121
Training: Private Studio, behind 517 Merrow St
ARMADALE, VIC, 3143

Requirements
Must have
• Must have logo (see attached) please not the one we use is the top left (blue and green)
please note attachment is top left (green and blue)

needs to be clear to read - the font needs to be clear and sharp and the background cannot be too busy.eg funny patterns.
Could I please see a card with a line for 'appointment time/date:' possibly on the back. Would like to see what this looks like.
Nell Wardrop's Profile (side of card) must include "Accredited Practicing Dietitian" and "Personal Trainer."
I like when the services plum stride provide are in dot form.
Nice to have
• would like the card to be 2 sides
first side:
Plum stride logo - Large
services plum stride provides: Dietetic/nutrition Consultations, weight loss coaching programs, personal and group training, post injury rehab, health and nutrition presentations and Health Retreats.
web address
second side:
smaller logo
Details for Nell:
Accredited Practicing Dietitian
Personal Trainer
Contact Details:
M: 0431907265
E: plumstride@postwren.com
Address:
Richmond VIC 3121
ARMADALE, VIC, 3143
Should not have
• Dietetic + nutrition consultations
Should say dietetic/nutrition consultations (first letter of words in capitals please)
Please write phone number as 0431 907 265
Not: 04 31 907265
- note numbers as 4, 3, 3.

```html
<!DOCTYPE html>
<html lang="en">
<head>
<meta charset="utf-8">
<title>Plum Stride Business Card</title>
<link rel="stylesheet" href="https://fonts.googleapis.com/css2?family=Arimo:ital,wght@0,400;0,700;1,400;1,700&family=Tinos:wght@400;700&display=swap">
<style>
  :root {
    --backdrop: #b8c6d2;
    --card-deep: #0b1322;
    --card-mid: #1d2a3f;
    --card-light: #2c3b54;
    --magenta: #e23fd9;
    --brand-blue: #2f62e6;
    --brand-green: #8be02a;
    --ink-white: #f2f4f8;
    --tape-yellow: #f1e40c;
    --tape-edge: #b9ad00;
    --pill-blue: #2357e0;
    --pill-text: #b6f23a;
  }
  * { box-sizing: border-box; margin: 0; padding: 0; }
  html, body {
    width: 1200px;
    height: 934px;
    overflow: hidden;
    background: var(--backdrop);
  }
  .card {
    position: absolute;
    left: 240px;
    width: 720px;
    height: 440px;
    border-radius: 3px;
    overflow: hidden;
    background:
      repeating-linear-gradient(0deg, rgba(255,255,255,0.025) 0 1px, transparent 1px 8px),
      repeating-linear-gradient(90deg, rgba(255,255,255,0.025) 0 1px, transparent 1px 8px),
      radial-gradient(ellipse at 60% 30%, var(--card-light) 0%, var(--card-mid) 45%, var(--card-deep) 100%);
    box-shadow: 0 6px 18px rgba(0,0,0,0.25);
  }
  .card--profile { top: 18px; }
  .card--services { top: 476px; }

  .brand {
    position: absolute;
    display: flex;
    align-items: center;
    gap: 12px;
  }
  .brand__dot {
    width: 34px;
    height: 34px;
    border-radius: 50%;
    background: var(--brand-green);
  }
  .brand__name {
    font-family: "Arimo", sans-serif;
    font-weight: 400;
    font-size: 46px;
    color: var(--brand-blue);
    letter-spacing: -0.5px;
  }
  .tagline {
    position: absolute;
    font-family: "Arimo", sans-serif;
    font-style: italic;
    font-size: 14px;
    color: var(--ink-white);
  }

  /* profile side */
  .card--profile .brand { left: 56px; top: 92px; }
  .card--profile .tagline { left: 104px; top: 150px; }
  .contact {
    position: absolute;
    left: 330px;
    top: 78px;
    width: 360px;
    text-align: center;
    font-family: "Tinos", serif;
    color: var(--ink-white);
  }
  .contact__name {
    font-weight: 700;
    font-size: 22px;
    color: var(--magenta);
  }
  .contact__role {
    font-weight: 700;
    font-size: 13px;
    margin-bottom: 8px;
  }
  .contact__line {
    font-size: 17px;
    line-height: 1.45;
  }
  .address {
    position: absolute;
    left: 40px;
    top: 330px;
    font-family: "Tinos", serif;
    font-size: 18px;
    line-height: 1.5;
    color: var(--ink-white);
  }

  /* services side */
  .card--services .brand { left: 44px; top: 150px; }
  .card--services .tagline { left: 92px; top: 208px; }
  .services {
    position: absolute;
    list-style: none;
    font-family: "Arimo", sans-serif;
    font-size: 19px;
    line-height: 1.45;
    color: var(--magenta);
  }
  .services--left { left: 44px; top: 246px; }
  .services--right { left: 410px; top: 96px; }
  .mobile-burst {
    position: absolute;
    left: 520px;
    top: 6px;
    width: 170px;
    height: 92px;
  }
  .mobile-burst__text {
    position: absolute;
    inset: 0;
    display: flex;
    flex-direction: column;
    align-items: center;
    justify-content: center;
    font-family: "Arimo", sans-serif;
    font-weight: 700;
    font-style: italic;
    font-size: 14px;
    line-height: 1.15;
    color: #3a9c12;
    text-align: center;
  }
  .web-pill {
    position: absolute;
    left: 44px;
    top: 352px;
    padding: 4px 16px;
    border-radius: 14px;
    background: var(--pill-blue);
    font-family: "Arimo", sans-serif;
    font-weight: 700;
    font-size: 15px;
    color: var(--pill-text);
  }
  .tape {
    position: absolute;
    left: 0;
    bottom: 0;
    width: 720px;
    height: 110px;
  }
</style>
</head>
<body>

<section class="card card--profile">
  <div class="brand">
    <span class="brand__dot"></span>
    <span class="brand__name">Plum Stride</span>
  </div>
  <p class="tagline">"it's what you put in!"</p>

  <div class="contact">
    <p class="contact__name">Nell Wardrop</p>
    <p class="contact__role">(Accredited Practicing Dietitian &amp; Personal trainer)</p>
    <p class="contact__line">Mobile: 0431907265</p>
    <p class="contact__line">E-mail: plumstride@postwren.com</p>
    <p class="contact__line">Web: www.plumstride.com.au</p>
  </div>

  <div class="address">
    <p>Address: Dietetics: Level 1, 88 Tolley Street Richmond VIC 3121</p>
    <p>Training: Private Studio, behind 517 Merrow St Armadale, VIC, 3143</p>
  </div>
</section>

<section class="card card--services">
  <div class="brand">
    <span class="brand__dot"></span>
    <span class="brand__name">Plum Stride</span>
  </div>
  <p class="tagline">"it's what you put in!"</p>

  <ul class="services services--left">
    <li>Dietetic/Nutrition Consultations</li>
    <li>Personal &amp; Group Training</li>
    <li>Health &amp; Nutrition Presentations</li>
  </ul>
  <ul class="services services--right">
    <li>Weight Loss Coaching Programs</li>
    <li>Post Injury Rehab</li>
    <li>Health Retreats</li>
  </ul>

  <div class="mobile-burst">
    <svg width="170" height="92" viewBox="0 0 170 92">
      <polygon fill="#ffffff"
        points="85,2 98,16 120,6 124,22 150,16 144,34 168,40 148,52 162,70 138,70 136,90 114,78 96,92 84,78 66,90 58,74 34,84 34,66 8,66 22,50 2,40 24,32 16,14 42,20 48,4 68,16"/>
    </svg>
    <div class="mobile-burst__text"><span>Mobile services</span><span>also available</span></div>
  </div>

  <p class="web-pill">www.plumstride.com.au</p>

  <svg class="tape" viewBox="0 0 720 110" role="img" aria-label="Yellow measuring tape running along the bottom edge">
    <path d="M0,88 C200,70 430,70 560,40 C620,26 680,10 720,4 L720,34 C680,40 630,54 570,70 C440,100 210,104 0,110 Z"
      fill="var(--tape-yellow)" stroke="var(--tape-edge)" stroke-width="1"/>
  </svg>
</section>

</body>
</html>
```